Business Card Design Project

I need a new business card for side business. Very simple and to the point. I am a licensed massage therapist and want the colors to be warm. I don't have a logo or company name. I just need to convey that I am a Licensed Massage Therapist and have my contact information so people can contact me. I'll attach some files that I like. I am a male so I don't want it to be feminine.

One file is my existing card. I like Tamsin's card and the layout so would prefer a similar layout. I would like to incorporate my swimmer/biker/runner image. Doesn't have to be the exact likeness because I don't have that file but something similar to that. I would like to also include my areas of specialty of: Swedish, Deep Tissue, Sports, and Hot Stone

I would also like to incorporate a QR code on the back of the card centered.
Updates

Payment is NOW guaranteed to the design I choose.  I updated my creative brief so hopefully it is more clear.  

Industry/Entity Type

Massage

Requirements
Must have
• Gavin Thrushwell
Licensed Massage Therapist
or
Massage Therapy
203-555-0187
gthrushwell@mailvale.net

```html
<!DOCTYPE html>
<html lang="en">
<head>
<meta charset="utf-8">
<title>Gavin Thrushwell — Licensed Massage Therapist</title>
<link rel="stylesheet" href="https://fonts.googleapis.com/css2?family=PT+Sans:ital,wght@0,400;0,700;1,700&family=PT+Sans+Narrow:wght@700&family=Tangerine:wght@700&display=swap">
<style>
  :root {
    --paper: #e6dccb;
    --rule-dark: #a48a63;
    --rule-light: #f4ede1;
    --ink-tan: #a88c60;
    --ink-brown: #5a3b16;
    --ink-deep: #3d2a12;
  }
  * { margin: 0; padding: 0; box-sizing: border-box; }
  html, body { width: 1200px; height: 720px; overflow: hidden; background: var(--paper); }
  .card {
    position: relative;
    width: 1200px;
    height: 720px;
    overflow: hidden;
    background:
      radial-gradient(ellipse 75% 70% at 50% 50%, rgba(255,255,255,0) 55%, rgba(120,90,50,0.38) 100%),
      linear-gradient(var(--paper), var(--paper));
  }
  .paper-texture {
    position: absolute;
    inset: 0;
    width: 1200px;
    height: 720px;
    opacity: 0.32;
    mix-blend-mode: multiply;
  }
  .rule {
    position: absolute;
    left: 0;
    width: 1200px;
    height: 4px;
    background: var(--rule-dark);
    box-shadow: 0 2px 0 var(--rule-light), 0 -1px 0 rgba(90,60,25,0.25);
  }
  .rule--top { top: 80px; }
  .rule--upper { top: 182px; }
  .rule--lower { top: 548px; }
  .rule--bottom { top: 636px; }
  .divider {
    position: absolute;
    left: 370px;
    top: 184px;
    width: 4px;
    height: 364px;
    background: var(--rule-dark);
    box-shadow: 2px 0 0 var(--rule-light);
  }
  .tagline {
    position: absolute;
    top: 96px;
    left: 0;
    width: 1200px;
    text-align: center;
    font-family: "PT Sans Narrow", sans-serif;
    font-weight: 700;
    font-size: 60px;
    line-height: 72px;
    letter-spacing: 4px;
    color: var(--ink-tan);
    text-shadow: 0 1px 0 var(--rule-light);
  }
  .specialties {
    position: absolute;
    left: 86px;
    top: 240px;
    list-style: none;
    font-family: "PT Sans", sans-serif;
    font-weight: 700;
    font-size: 42px;
    line-height: 65px;
    letter-spacing: 2.5px;
    color: var(--ink-tan);
    text-shadow: 0 1px 0 var(--rule-light);
  }
  .therapist-name {
    position: absolute;
    left: 374px;
    width: 826px;
    top: 268px;
    text-align: center;
    font-family: "Tangerine", cursive;
    font-weight: 700;
    font-size: 136px;
    line-height: 1;
    color: var(--ink-brown);
    text-shadow: 0 1px 0 rgba(255,255,255,0.4);
    white-space: nowrap;
  }
  .credential {
    position: absolute;
    right: 102px;
    top: 490px;
    font-family: "PT Sans", sans-serif;
    font-style: italic;
    font-weight: 700;
    font-size: 25px;
    color: var(--ink-deep);
  }
  .contact {
    position: absolute;
    top: 570px;
    left: 0;
    width: 1200px;
    text-align: center;
    font-family: "PT Sans", sans-serif;
    font-weight: 700;
    font-size: 35px;
    letter-spacing: 3.5px;
    color: var(--ink-tan);
    text-shadow: 0 1px 0 var(--rule-light);
    white-space: nowrap;
  }
  .contact__sep { margin: 0 26px; }
</style>
</head>
<body>
  <main class="card">
    <svg class="paper-texture" viewBox="0 0 1200 720" aria-hidden="true">
      <filter id="canvas-grain">
        <feTurbulence type="fractalNoise" baseFrequency="0.55" numOctaves="3" seed="4"/>
        <feColorMatrix type="saturate" values="0"/>
      </filter>
      <rect width="1200" height="720" filter="url(#canvas-grain)"/>
    </svg>

    <div class="rule rule--top"></div>
    <h2 class="tagline">WHERE YOUR HEALING IS IN OUR HANDS</h2>
    <div class="rule rule--upper"></div>

    <ul class="specialties">
      <li>Swedish</li>
      <li>Deep Tissue</li>
      <li>Sports</li>
      <li>Hot Stone</li>
    </ul>
    <div class="divider"></div>

    <h1 class="therapist-name">Gavin Thrushwell</h1>
    <p class="credential">Licensed Massage Therapist</p>

    <div class="rule rule--lower"></div>
    <p class="contact">
      <span class="contact__phone">T:203 555 0187</span><span class="contact__sep">|</span><span class="contact__email">gthrushwell@mailvale.net</span>
    </p>
    <div class="rule rule--bottom"></div>
  </main>
</body>
</html>
```